Halvard Atelier Business cards

Design our business cards and eventually a logo. The company is based in Paris, its activity is the retailing via internet of luxury home furniture (like Vambrelli, Bercusa, tarvoni...) Our clients are international andwith a high sense of aesthetics. The design shall communicate wealth and trust with a high quality and aesthetic sense, pure lines Company Name is Halvard AtelierExplanation of the name: usually people who wants to buy furniture usually go in a showroom. Today they go in showroom to test the furniture and they search for the price on internet, which is a "Halvard atelier".We will not be a e-commerce site. Our site will be (another project) a presentation site which purpose is to reach qualified prospects. Then everything will be handled by phone, meeting etc.The business card must be professional as we will negotiate with many luxury brands, opportunity to represent them on our site, prices etc.As far as the color are concerned mostly black and whithe or grey. The font of the Halvard Atelier name shall have some impact.

Target Market(s)

High-end furniture and buyers of luxury goods, international customers, mostly women who handle such projects.
We also deal with professional buyers (hotels as an example) and luxury brands

Contact Information for Business Card

standard format 85x55, lanscape card, square corners will be printed on thick high quality paper (300 or 350g)

Font styles to use
Sans Serif

Colors

Designer to choose colors to be used in the design.

Requirements
Must have
• Must be white, as the paper will be high quality, the paper will enhance the card.
• Name of the brand Halvard atelier (with specific font which make it very nice looking and catch the attention. similar to Calibri or Calibri
• Name of person (will give you the name later (4 names and position)
• the position of the person
• Mobile phone, e-mail, Physical address 27, rue Fenouillard, 75005 Paris, France (courrier only) our web site www.halvardatelier.fr
• The card must be simple and class
Nice to have
• Font of the address is smaller than the rest,
• Calibri font or similar on recto side with the name of the company which may look similar to the picture inserted in the brief.
• The grey color in the picture inserted is ok for us
Should not have
• Any parallel lines which represent the name of the company
• Any heavy design If you go on internet sites which present the furniture all designs are pure lines and high quality craftsmanship. To have an idea of our targetted client or brand we will be in touch: https://www.casavelumi.it/projects/
• Note that the picture added below is what we use, now as mail signature, up to you to have a better design etc.

```html
<!DOCTYPE html>
<html lang="en">
<head>
<meta charset="UTF-8">
<title>Halvard Atelier SAS – Business cards</title>
<link href="https://fonts.googleapis.com/css2?family=Open+Sans:wght@300;400;600;700&display=swap" rel="stylesheet">
<style>
  :root {
    --backdrop: #262626;
    --paper: #ecebe6;
    --ink: #6b6b69;
    --ink-soft: #7a7a77;
    --rule: #8a8a86;
  }
  * { margin: 0; padding: 0; box-sizing: border-box; }
  html, body {
    width: 1200px;
    height: 750px;
    overflow: hidden;
    background: var(--backdrop);
    font-family: "Open Sans", sans-serif;
  }
  .stage {
    width: 1200px;
    height: 750px;
    display: flex;
    align-items: center;
    justify-content: center;
    gap: 60px;
  }
  .card {
    position: relative;
    width: 520px;
    height: 336px;
    background: var(--paper);
    overflow: hidden;
  }
  /* Recto */
  .card--front {
    display: flex;
    align-items: center;
    justify-content: center;
  }
  .brand-title {
    font-weight: 700;
    font-size: 34px;
    color: var(--ink);
    letter-spacing: 0.2px;
  }
  /* Verso: content set vertically, reading bottom to top */
  .back-layout {
    position: absolute;
    width: 336px;
    height: 520px;
    left: 50%;
    top: 50%;
    transform: translate(-50%, -50%) rotate(-90deg);
    padding: 34px 0 0 52px;
  }
  .back-brand {
    font-weight: 700;
    font-size: 23px;
    color: var(--ink);
    margin-bottom: 62px;
  }
  .detail-block {
    width: 205px;
    border-top: 1px solid var(--rule);
    border-left: 1px solid var(--rule);
    padding: 6px 0 6px 10px;
    margin-bottom: 50px;
    color: var(--ink-soft);
  }
  .person-name {
    font-weight: 600;
    font-size: 15px;
    color: var(--ink);
    line-height: 1.2;
  }
  .person-role {
    font-weight: 300;
    font-size: 15px;
    line-height: 1.2;
  }
  .contact-line {
    font-weight: 400;
    font-size: 12px;
    line-height: 1.45;
  }
</style>
</head>
<body>
  <main class="stage">
    <section class="card card--front" aria-label="Card front">
      <h1 class="brand-title">Halvard Atelier SAS</h1>
    </section>

    <section class="card card--back" aria-label="Card back">
      <div class="back-layout">
        <p class="back-brand">Halvard Atelier SAS</p>
        <div class="detail-block">
          <p class="person-name">Elouan Varenne</p>
          <p class="person-role">President/Co-Founder</p>
        </div>
        <div class="detail-block">
          <p class="contact-line">+33647219085</p>
          <p class="contact-line">www.halvardatelier.fr</p>
        </div>
        <div class="detail-block">
          <p class="contact-line">27 rue Fenouillard</p>
          <p class="contact-line">75005 Paris, France</p>
        </div>
      </div>
    </section>
  </main>
</body>
</html>
```